Business Card Design for BrightwaveOutreach.com

--I need a business card design for my company BrightwaveOutreach.com

I have attached my logo...I want the brightwave outreach logo on the front of the business card, and then I want The Brightwave Chief on the back of it with my information.

I would like to see a light colored background as well as a dark colored background

FRONT:
BRIGHTWAVE OUTREACH LOGO
482 N. Elmwood
3rd Floor
San Diego CA 92101
www.BrightwaveOutreach.com

Advanced Website & App Development
Websites, Apps, Online Voucher Systems

Leading Edge Marketing Services
SMS, VB, SMM, SEM,

BACK:
BRIGHTWAVE CHIEF LOGO
Dorian Pelley
The Brightwave Chief
Call Or Text: 619-555-0148
Dorian@BrightwaveChief.com
www.BrightwaveChief.com

Target Market(s)

small business owners

Industry/Entity Type

Business Consultant

Contact Information for Business Card

FRONT:
BRIGHTWAVE OUTREACH LOGO
482 N. Elmwood
3rd Floor
San Diego CA 92101
www.BrightwaveOutreach.com

SMS, VB, SMM, SEM,

BACK:
BRIGHTWAVE CHIEF LOGO
Dorian Pelley
The Brightwave Chief
Dorian@BrightwaveChief.com
www.BrightwaveChief.com

Requirements
Must have
• add this quote on it somewhere, anywhere,preferrably on back
• "The Fastest Way To Success Is To Take Action”
• — Dorian Pelley, Brightwave Chief
Nice to have
• open
Should not have
• red

```html
<!DOCTYPE html>
<html lang="en">
<head>
<meta charset="utf-8">
<title>Brightwave Outreach Business Cards</title>
<link rel="stylesheet" href="https://fonts.googleapis.com/css2?family=Exo+2:ital,wght@0,300;0,400;0,500;1,400&display=swap">
<style>
  :root {
    --page: #5b5a58;
    --card: #231f20;
    --band: #0f73b6;
    --brand-blue: #1a7fc2;
    --muted: #8c8c8c;
    --light: #f2f4f6;
  }
  * { margin: 0; padding: 0; box-sizing: border-box; }
  html, body { width: 1200px; height: 900px; overflow: hidden; }
  body {
    background: var(--page);
    font-family: "Exo 2", sans-serif;
    display: flex;
    flex-direction: column;
    align-items: center;
    justify-content: center;
    gap: 36px;
  }
  .card {
    width: 740px;
    height: 404px;
    background: var(--card);
    position: relative;
    box-shadow: 0 10px 24px rgba(0,0,0,.35);
    overflow: hidden;
  }
  .band {
    background: var(--band);
    color: var(--light);
    text-align: center;
  }

  /* Back: the chief card */
  .card-back .wordmark {
    position: absolute;
    top: 26px;
    right: 74px;
    font-size: 50px;
    font-weight: 500;
    letter-spacing: 4px;
    color: var(--brand-blue);
  }
  .card-back .quote-band {
    position: absolute;
    top: 110px;
    left: 0; right: 0;
    height: 58px;
    padding-top: 8px;
    font-style: italic;
    font-size: 16px;
    line-height: 21px;
    letter-spacing: 1px;
  }
  .card-back .identity {
    position: absolute;
    top: 186px;
    right: 60px;
    text-align: right;
  }
  .card-back .name {
    font-size: 36px;
    font-weight: 400;
    letter-spacing: 3px;
    color: var(--brand-blue);
    line-height: 36px;
  }
  .card-back .title {
    font-size: 26px;
    font-weight: 300;
    letter-spacing: 2px;
    color: var(--muted);
    line-height: 28px;
  }
  .contact-list {
    position: absolute;
    top: 276px;
    right: 60px;
    list-style: none;
    text-align: right;
  }
  .contact-list li {
    display: flex;
    justify-content: flex-end;
    align-items: center;
    gap: 10px;
    font-size: 20px;
    letter-spacing: 1.5px;
    color: var(--muted);
    line-height: 28px;
  }
  .contact-list .accent { color: var(--brand-blue); }
  .contact-list svg { width: 20px; height: 20px; flex: none; }

  /* Front: the company card */
  .card-front .address-band {
    position: absolute;
    top: 0; left: 0; right: 0;
    height: 92px;
    padding-top: 20px;
    font-size: 21px;
    line-height: 26px;
    letter-spacing: 1.5px;
  }
  .card-front .site {
    position: absolute;
    top: 104px;
    left: 0; right: 0;
    text-align: center;
    font-size: 20px;
    letter-spacing: 1.5px;
    color: var(--muted);
  }
  .card-front .site .accent { color: var(--brand-blue); }
  .card-front .wordmark {
    position: absolute;
    top: 138px;
    left: 0; right: 0;
    text-align: center;
    font-size: 52px;
    font-weight: 500;
    letter-spacing: 4px;
    color: var(--brand-blue);
  }
  .card-front .rule {
    position: absolute;
    top: 220px;
    height: 2px;
    width: 120px;
    background: var(--muted);
  }
  .card-front .rule.left { left: 70px; }
  .card-front .rule.right { right: 70px; }
  .card-front .services-band {
    position: absolute;
    top: 246px;
    left: 0; right: 0;
    height: 80px;
    padding-top: 12px;
    font-size: 23px;
    line-height: 28px;
    letter-spacing: 1.5px;
  }
  .card-front .marketing {
    position: absolute;
    top: 336px;
    left: 0; right: 0;
    text-align: center;
    font-size: 23px;
    line-height: 28px;
    letter-spacing: 1.5px;
    color: var(--muted);
  }
</style>
</head>
<body>

<section class="card card-back" aria-label="Back of card">
  <div class="wordmark">BRIGHTWAVE CHIEF</div>
  <div class="band quote-band">
    <p>"The Fastest Way To Success Is To Take Action"</p>
    <p>— Dorian Pelley, Brightwave Chief</p>
  </div>
  <div class="identity">
    <p class="name">DORIAN PELLEY</p>
    <p class="title">The Brightwave Chief</p>
  </div>
  <ul class="contact-list">
    <li>619-555-0148
      <svg viewBox="0 0 20 20" aria-hidden="true"><circle cx="10" cy="10" r="10" fill="var(--brand-blue)"/><rect x="7" y="4.5" width="6" height="11" rx="1.2" fill="none" stroke="var(--card)" stroke-width="1.4"/></svg>
    </li>
    <li>Dorian@BrightwaveChief.com
      <svg viewBox="0 0 20 20" aria-hidden="true"><circle cx="10" cy="10" r="10" fill="var(--brand-blue)"/><rect x="5" y="6.5" width="10" height="7" fill="none" stroke="var(--card)" stroke-width="1.3"/><path d="M5 6.5 L10 11 L15 6.5" fill="none" stroke="var(--card)" stroke-width="1.3"/></svg>
    </li>
    <li><span>www.<span class="accent">BrightwaveChief</span>.com</span>
      <svg viewBox="0 0 20 20" aria-hidden="true"><circle cx="10" cy="10" r="10" fill="var(--brand-blue)"/><circle cx="10" cy="10" r="5.5" fill="none" stroke="var(--card)" stroke-width="1.2"/><ellipse cx="10" cy="10" rx="2.4" ry="5.5" fill="none" stroke="var(--card)" stroke-width="1.2"/><line x1="4.5" y1="10" x2="15.5" y2="10" stroke="var(--card)" stroke-width="1.2"/></svg>
    </li>
  </ul>
</section>

<section class="card card-front" aria-label="Front of card">
  <div class="band address-band">
    <p>482 N. Elmwood, 3rd Floor</p>
    <p>San Diego CA 92101</p>
  </div>
  <p class="site">www.<span class="accent">BrightwaveOutreach</span>.com</p>
  <div class="wordmark">BRIGHTWAVE OUTREACH</div>
  <span class="rule left"></span>
  <span class="rule right"></span>
  <div class="band services-band">
    <p>Advanced Website &amp; App Development</p>
    <p>Websites, Apps, Online Voucher Systems</p>
  </div>
  <div class="marketing">
    <p>Leading Edge Marketing Services</p>
    <p>SMS, VB, SMM, SEM,</p>
  </div>
</section>

</body>
</html>
```